Geschäftspapiere für Immobilienmakler
Tolles Design. Schnelle Umsetzung der Änderungswünsche.
Zielgruppe
Wir sind Immobilienmakler und bieten zusätzlich Home Staging an.
https://nordhaus-kellwang.de/Home-Staging/
Um anderen Immobilienmakler oder Privatanbieter unsere Dienstleistung anzubieten, möchten wir ein Anschreiben gestalten lassen. Welches wir hauptsächlich per E-Mail versenden können, da die Postanschrift oft nicht bekannt ist.
Trotzdem bitte auch eine Rückseite gestalten für den Versand per Post.
Aufgabenstellung
Im Anhang ist ein Muster mit Mustertext.
Bitte auch eine Rückseite gestalten für den Versand per Post.
Das Anschreiben/der Infobrief sollte ansprechend schick aussehen.
Ich könne mir vorstellen, dass oben auf der Seite die gleichen Bilder sind wir auf der Homepage.
Oder dies in den Hintergrund miteingearbeitet wird.
(die Lampe, das Bett, die Badezimmerdeko)
Wichtig ist auch dass das Logo mit der Glühbirne, dem Vogel und dem Slogan 'Ins richtige Licht rücken - Werte steigern'
Weiterhin wichtig dass die Vorher-Nachher Bilder gut zur Geltung kommen.
Ich habe als Datei unsere Flyer und eine Mappe zur Ansicht mit angehängt.
Hier sollte es dazu passen.

```html
<!DOCTYPE html>
<html lang="de">
<head>
<meta charset="utf-8">
<title>Infobrief Home Staging – Nordhaus Kellwang</title>
<link rel="stylesheet" href="https://fonts.googleapis.com/css2?family=Arimo:wght@400;700&family=Nunito:wght@700;800&family=Tinos:wght@400;700&display=swap">
<style>
  :root{
    --navy:#0d4478;
    --gold:#b89038;
    --ink:#1c1c1c;
    --paper:#ffffff;
    --stage:#d4d4d4;
    --faint:#f1f1f1;
  }
  *{box-sizing:border-box;margin:0;padding:0}
  html,body{width:1117px;height:1200px;overflow:hidden;background:var(--stage)}
  .canvas{position:relative;width:1117px;height:1200px}
  .sheet{position:absolute;top:218px;width:740px;height:1046px;background:var(--paper);
    transform:scale(.73);transform-origin:top left;overflow:hidden}
  .sheet--front{left:12px}
  .sheet--back{left:565px}
  .abs{position:absolute}

  /* front */
  .rule{position:absolute;height:2px;background:var(--gold)}
  .slogan{font-family:"Nunito",sans-serif;font-weight:800;font-size:18px;line-height:24px}
  .slogan--left{right:365px;top:98px;text-align:right}
  .slogan--right{left:437px;top:98px}
  .navy{color:var(--navy)}
  .gold{color:var(--gold)}
  .slogan .big{font-size:20px}
  .slogan-dot{left:382px;top:48px;width:56px;height:56px;border:4px solid var(--gold);border-radius:50%}
  .letter{font-family:"Tinos",serif;color:var(--ink);font-size:11.5px;line-height:19px;left:102px;width:480px}
  .letter strong{font-weight:700}
  .letter .salutation{font-size:13.5px;font-weight:700;line-height:20px}
  .letter .subhead{color:var(--navy);font-weight:700}
  .photo{position:absolute}
  .photo--before{left:102px;top:490px;width:282px;height:204px;
    background:linear-gradient(180deg,#eef0ec 0%,#dfe3dc 55%,#b98a5a 70%,#c79a6b 100%)}
  .photo--after{left:419px;top:494px;width:284px;height:200px;
    background:linear-gradient(180deg,#f0f1ee 0%,#e1e4de 52%,#5b4a4a 64%,#a9a7a8 78%,#c6996a 100%)}
  .tag{position:absolute;font-family:"Arimo",sans-serif;color:#fff;font-size:19px;line-height:30px;padding-left:36px}
  .tag--navy{background:var(--navy);left:0;top:640px;width:168px}
  .tag--gold{background:var(--gold);left:0;top:680px;width:225px}
  .arrow{left:362px;top:640px}
  .footer-rule{left:0;top:958px;width:740px}
  .contact{font-family:"Arimo",sans-serif;font-weight:700;color:var(--navy);font-size:11.5px;line-height:15px;top:976px}
  .brand{font-family:"Arimo",sans-serif;font-weight:700;color:var(--navy);font-size:16px;line-height:19px;display:flex;align-items:center;gap:8px}
  .brand-mark{width:14px;height:14px;border-radius:50%;background:var(--gold);flex:none}
  .faint-pill{left:35px;top:914px;width:375px;height:50px;border-radius:25px;background:var(--faint)}

  /* back */
  .column{left:470px;top:0;width:270px;height:1046px;background:var(--navy)}
  .band{position:absolute;font-family:"Arimo",sans-serif;font-weight:700;color:#fff;font-size:19px;line-height:34px;padding-left:28px}
  .band--navy{background:var(--navy);left:0;top:78px;width:192px}
  .band--gold{background:var(--gold);left:0;top:116px;width:168px;line-height:32px}
  .portrait{position:absolute;width:210px;height:210px;border-radius:50%}
  .portrait--one{left:122px;top:226px;background:radial-gradient(circle at 50% 45%,#9c9c9c,#5e5e5e 70%,#bdbdbd)}
  .portrait--two{left:98px;top:520px;background:radial-gradient(circle at 45% 50%,#8d8d8d,#4f4f4f 70%,#b4b4b4)}
  .role{position:absolute;font-family:"Arimo",sans-serif;color:#fff;font-size:13px;line-height:28px;padding:0 10px}
  .role--navy{background:var(--navy);left:312px;top:262px}
  .role--gold{background:var(--gold);left:300px;top:554px}
  .signature{position:absolute;background:linear-gradient(90deg,rgba(40,40,40,.08),rgba(40,40,40,.16))}
  .signature--one{left:200px;top:348px;width:220px;height:80px}
  .signature--two{left:190px;top:640px;width:200px;height:80px}
  .gallery{position:absolute;left:500px;width:220px;height:198px}
  .gallery--bed{top:240px;background:linear-gradient(180deg,#f3f3f1,#d9d6d2 55%,#8a7f79)}
  .gallery--lamp{top:458px;background:linear-gradient(180deg,#efefef,#d8b35a 40%,#9c9a98 75%,#e4e4e4)}
  .gallery--bath{top:676px;background:linear-gradient(180deg,#f4f4f6,#dcdde2 60%,#b7a4b8)}
  .back-brand{left:500px;top:132px;color:#fff;font-size:20px}
  .back-brand .brand-mark{width:16px;height:16px}
  .refs{left:490px;top:936px;width:230px;font-family:"Arimo",sans-serif;font-weight:700;font-style:italic;color:#fff;font-size:12px}
  .url-box{left:490px;top:960px;background:var(--gold);font-family:"Arimo",sans-serif;font-weight:700;color:#fff;font-size:14px;line-height:30px;padding:0 12px}
</style>
</head>
<body>
<div class="canvas">

  <!-- Vorderseite: Anschreiben -->
  <section class="sheet sheet--front" aria-label="Anschreiben Home Staging">
    <div class="rule" style="left:102px;top:123px;width:138px"></div>
    <div class="rule" style="left:534px;top:123px;width:206px"></div>
    <p class="abs slogan slogan--left"><span class="navy">Ins richtige</span><br><span class="gold big">Licht</span> <span class="navy">rücken.</span></p>
    <div class="abs slogan-dot"></div>
    <p class="abs slogan slogan--right"><span class="gold big">Werte</span><br><span class="navy">steigern!</span></p>

    <div class="abs letter" style="top:188px">
      <p class="salutation">Sehr geehrte Damen und Herren,<br>liebe Kunden, liebe Kollegen,</p>
      <p style="margin-top:16px">bei Marktrecherchen ist unserem Backoffice aufgefallen dass wir Ihre Immobilie/Immobilien durch unsere verkaufsfördernden Maßnahmen in ein besseres Licht rücken können.<br><strong>Für einen erfolgreichen und schnelleren Verkauf bieten wir HOME STAGING an.</strong></p>
      <p style="margin-top:18px"><span class="subhead">Was ist HOME STAGING?</span><br>HOME STAGING wird das professionelle herrichten von Räumen oder ganzen Immobilie zur Verkaufsförderung genannt. Diese Adaption umfasst den gezielten Einsatz von Möbeln, Dekoration, Farbe, Licht, Wand- und Fußbodengestaltung.</p>
      <p style="margin-top:10px">Immobilien, die mit HOME STAGING für den Verkauf vorbereitet werden, haben eine viel kürzere Verkaufszeit und einen <strong>höheren Verkaufspreis um ca. 10-15%.</strong></p>
      <p style="margin-top:22px"><strong>Hier nur ein Beispiel:</strong></p>
    </div>

    <div class="photo photo--before" role="img" aria-label="Foto: leerer Wohnraum mit Erkerfenster vor dem Home Staging"></div>
    <div class="photo photo--after" role="img" aria-label="Foto: derselbe Wohnraum mit Sofa, Teppich und Pflanze nach dem Home Staging"></div>
    <div class="tag tag--navy">Vor und nach</div>
    <div class="tag tag--gold">dem Home Staging</div>
    <svg class="abs arrow" width="90" height="45" viewBox="0 0 90 45" aria-hidden="true">
      <path d="M2 40 C20 12 50 8 78 24" fill="none" stroke="var(--navy)" stroke-width="5" stroke-linecap="round"/>
      <path d="M66 12 L82 26 L62 32" fill="none" stroke="var(--navy)" stroke-width="5" stroke-linecap="round" stroke-linejoin="round"/>
    </svg>

    <div class="abs letter" style="top:736px">
      <p><span class="subhead">Probieren Sie es aus!</span><br>Anschließend werden Sie jede Immobilie Home Stagen lassen.<br>Gerne machen wir Ihnen ein unschlagbares Kennenlern-Angebot.</p>
      <p style="margin-top:50px"><strong>Mit freundlichen Grüßen<br>Jana und Paul Kellwang</strong></p>
    </div>
    <div class="abs faint-pill"></div>
    <p class="abs letter" style="top:928px">Weitere Infos unter: www.nordhaus-kellwang.de</p>

    <div class="rule footer-rule"></div>
    <p class="abs contact" style="left:100px">Nordhaus Kellwang<br>Immobilien GmbH<br>Lindenweg 8<br>24103 Kiel</p>
    <p class="abs contact" style="left:266px">Tel.: 0 43 12 / 55 60 21<br>Fax: 0 43 12 / 55 60 29<br>kontakt@nordhaus-kellwang.de<br>www.nordhaus-kellwang.de</p>
    <div class="abs brand" style="left:528px;top:996px"><span class="brand-mark"></span>Nordhaus Kellwang</div>
  </section>

  <!-- Rückseite -->
  <section class="sheet sheet--back" aria-label="Rückseite Infobrief">
    <div class="abs column"></div>
    <div class="band band--navy">Wir verschönern</div>
    <div class="band band--gold">Ihre Immobilie</div>
    <svg class="abs" style="left:168px;top:130px" width="320" height="30" aria-hidden="true">
      <path d="M0 2 L320 22" stroke="var(--gold)" stroke-width="2"/>
    </svg>
    <div class="abs brand back-brand"><span class="brand-mark"></span>Nordhaus Kellwang</div>

    <div class="portrait portrait--one" role="img" aria-label="Porträtfoto der Immobilienmaklerin Jana Kellwang"></div>
    <div class="role role--navy">Immobilienmaklerin</div>
    <div class="signature signature--one" role="img" aria-label="Unterschrift Jana Kellwang"></div>

    <div class="portrait portrait--two" role="img" aria-label="Porträtfoto des Geschäftsführers Paul Kellwang"></div>
    <div class="role role--gold">Geschäftsführer</div>
    <div class="signature signature--two" role="img" aria-label="Unterschrift Paul Kellwang"></div>

    <div class="gallery gallery--bed" role="img" aria-label="Foto: gestaltetes Schlafzimmer mit Bett und Spiegel"></div>
    <div class="gallery gallery--lamp" role="img" aria-label="Foto: Leuchte mit goldenem Schirm"></div>
    <div class="gallery gallery--bath" role="img" aria-label="Foto: dekoriertes Badezimmer unter der Dachschräge"></div>

    <svg class="abs" style="left:0;top:900px" width="490" height="60" aria-hidden="true">
      <path d="M0 2 L490 56" stroke="var(--gold)" stroke-width="2"/>
    </svg>
    <p class="abs refs">weitere Referenzen finden Sie unter:</p>
    <div class="abs url-box">www.nordhaus-kellwang.de</div>
  </section>

</div>
</body>
</html>
```